Business card design for event company

need design double sided in square shape ( approx 6x6cm) in matt grey shades
front side :
logo ( could be in one color like picture attached ) printpress effect in a rect box

back side :
name in big font with silver foil finish ( similar to attached pic )

phone number i would like to see how it will look like if embossed ( like in credit cards )

Sample for contact on card ( will need 5 different contacts) - pls. include small icons next to each contact

KARIM SALEHI
Managing Director

+971 50 374 6619
karim@novlinkuae.com
www.novlink.ae
Building C2 , Office 318
Marsa Tirel Park

Please consider this is an urgent project . thank you in advance

```html
<!DOCTYPE html>
<html lang="en">
<head>
<meta charset="utf-8">
<title>Novlink – Business Card</title>
<link href="https://fonts.googleapis.com/css2?family=Lato:wght@300;400;700;900&display=swap" rel="stylesheet">
<style>
  :root {
    --stage: #2a2a2a;
    --orange: #e98f29;
    --paper: #efefef;
    --ink: #4f4f4f;
    --ink-soft: #6a6a6a;
    --white: #ffffff;
  }
  * { margin: 0; padding: 0; box-sizing: border-box; }
  html, body { width: 1200px; height: 900px; overflow: hidden; }
  body {
    background: var(--stage);
    font-family: "Lato", sans-serif;
    display: flex;
    align-items: center;
    justify-content: center;
    gap: 60px;
  }
  .card {
    width: 460px;
    height: 460px;
    border-radius: 22px;
    position: relative;
    overflow: hidden;
  }
  .card--front { background: var(--orange); }
  .card--back { background: var(--paper); }

  .brand {
    position: absolute;
    left: 0;
    width: 100%;
    display: flex;
    align-items: center;
    justify-content: center;
    gap: 14px;
  }
  .card--front .brand { top: 180px; }
  .card--back .brand { top: 44px; }
  .brand-mark { width: 16px; height: 16px; }
  .brand-name {
    font-weight: 700;
    font-size: 52px;
    letter-spacing: 1px;
    line-height: 1;
    color: var(--ink);
  }
  .card--front .brand-mark { background: var(--ink); }
  .card--back .brand-mark { background: var(--orange); }

  .website {
    position: absolute;
    bottom: 54px;
    width: 100%;
    text-align: center;
    color: var(--white);
    font-weight: 700;
    font-size: 14px;
    letter-spacing: 6px;
  }

  .holder {
    position: absolute;
    left: 50px;
    top: 136px;
  }
  .holder-name {
    font-size: 44px;
    line-height: 1;
    color: var(--ink);
  }
  .holder-name .first { font-weight: 900; }
  .holder-name .last { font-weight: 300; color: var(--orange); }
  .holder-title {
    display: inline-block;
    margin-top: 8px;
    background: var(--orange);
    color: var(--white);
    font-weight: 700;
    font-size: 18px;
    padding: 5px 18px;
  }
  .contacts {
    position: absolute;
    left: 74px;
    top: 262px;
    list-style: none;
    display: flex;
    flex-direction: column;
    gap: 11px;
  }
  .contact {
    display: flex;
    align-items: center;
    gap: 12px;
    color: var(--ink-soft);
    font-size: 17px;
    line-height: 22px;
  }
  .contact svg { width: 18px; height: 18px; flex: none; }
</style>
</head>
<body>
  <section class="card card--front" aria-label="Card front">
    <div class="brand">
      <span class="brand-mark"></span>
      <span class="brand-name">Novlink</span>
    </div>
    <p class="website">www.novlink.ae</p>
  </section>

  <section class="card card--back" aria-label="Card back">
    <div class="brand">
      <span class="brand-mark"></span>
      <span class="brand-name">Novlink</span>
    </div>

    <div class="holder">
      <h1 class="holder-name"><span class="first">Karim</span> <span class="last">Salehi</span></h1>
      <p class="holder-title">Chief Executive Offer</p>
    </div>

    <ul class="contacts">
      <li class="contact">
        <svg viewBox="0 0 24 24" aria-hidden="true"><path fill="#e98f29" d="M6.6 10.8a15.5 15.5 0 0 0 6.6 6.6l2.2-2.2a1 1 0 0 1 1-.25 11.4 11.4 0 0 0 3.6.57 1 1 0 0 1 1 1V20a1 1 0 0 1-1 1A17 17 0 0 1 3 4a1 1 0 0 1 1-1h3.5a1 1 0 0 1 1 1c0 1.25.2 2.45.57 3.57a1 1 0 0 1-.25 1z"/></svg>
        <span>+971 50 374 6619</span>
      </li>
      <li class="contact">
        <svg viewBox="0 0 24 24" aria-hidden="true"><rect x="2" y="5" width="20" height="14" fill="#e98f29"/><polyline points="2,5 12,13 22,5" fill="none" stroke="#fff" stroke-width="1.8"/></svg>
        <span>karim@novlinkuae.com</span>
      </li>
      <li class="contact">
        <svg viewBox="0 0 24 24" aria-hidden="true"><circle cx="12" cy="12" r="9" fill="none" stroke="#e98f29" stroke-width="2"/><ellipse cx="12" cy="12" rx="4" ry="9" fill="none" stroke="#e98f29" stroke-width="1.6"/><line x1="3" y1="12" x2="21" y2="12" stroke="#e98f29" stroke-width="1.6"/></svg>
        <span>www.novlink.ae</span>
      </li>
      <li class="contact">
        <svg viewBox="0 0 24 24" aria-hidden="true"><rect x="5" y="3" width="14" height="18" fill="#e98f29"/><rect x="8" y="6" width="3" height="3" fill="#fff"/><rect x="13" y="6" width="3" height="3" fill="#fff"/><rect x="8" y="11" width="3" height="3" fill="#fff"/><rect x="13" y="11" width="3" height="3" fill="#fff"/><rect x="10.5" y="16" width="3" height="5" fill="#fff"/></svg>
        <span>Building C2 , Office 318</span>
      </li>
      <li class="contact">
        <svg viewBox="0 0 24 24" aria-hidden="true"><path fill="#e98f29" d="M12 2a7 7 0 0 0-7 7c0 5 7 13 7 13s7-8 7-13a7 7 0 0 0-7-7zm0 9.5A2.5 2.5 0 1 1 12 6.5a2.5 2.5 0 0 1 0 5z"/></svg>
        <span>Marsa Tirel Park</span>
      </li>
    </ul>
  </section>
</body>
</html>
```